DOVR Business Card Design Project

Company Name: DOVR (Dove Operational Versatile Resources) JLT.
Office Address: Office No 218, Saffron Crest Tower, Palmera Bay Towers, Dubai, U.A.E
Company line of business:
1) Currently we have a POS solution for retail outlets like duty free shops, supermarkets, department stores etc... The solution is deployed in Harbor Gate Retail on 350 POS and in Coralline Port Retail on 100 POS. So our main line of business is the deployment of this solution in retail outlets locally or regionally. We have already deployed the solution in India and Australia.
2) Integration of other third party POS systems with an online credit authorization netwotk in the UAE. This will enable POS applications to connect directly to the acquiring banks without needing an EFT terminal like Paxoline or Tramodex. The credit card payment is completed at the POS.
3) Other solutions that are targeting retail outlets like mobile POS, queue busting solutions, stock taking solutions using hand held devices, transaction capture systems, etc...
4) Other IT services like support of call center solutions from Bramwell Systems and development of new solutions as per customer requirements.
We need a business card design for the company. We don't have any specific requirements and will eave up to the designers to come up with creative designs. At the moment we still don't have a letter head design and the only thing that we have is the company logo that we will upload shortly.
Updates
Dear All,
I just uploaded the logo source files. I am sorry for the delay.
Regards
Tarek Demirci
I would like the business cards to have the following details:
Company Tel No
Company Fax No
Company Website Address
Employee Name
Employee Title
Employee Mobile Number
Employee Email Address

```html
<!DOCTYPE html>
<html lang="en">
<head>
<meta charset="utf-8">
<title>DOVR Business Card</title>
<link href="https://fonts.googleapis.com/css2?family=Ubuntu:wght@400;500&display=swap" rel="stylesheet">
<style>
  :root {
    --backdrop: #d9d9d6;
    --card-black: #151515;
    --card-black-soft: #222222;
    --card-white: #ffffff;
    --band-red: #c4161c;
    --band-red-dark: #8e0e12;
    --ink: #1a1a1a;
    --text-light: #ffffff;
    --text-muted: #e6e6e6;
    --mark-blue: #1f6fc6;
  }
  * { box-sizing: border-box; margin: 0; padding: 0; }
  html, body {
    width: 1200px; height: 900px; overflow: hidden;
    background: var(--backdrop);
    font-family: "Ubuntu", sans-serif;
  }
  .canvas { position: relative; width: 1200px; height: 900px; }
  .card {
    position: absolute; top: 142px;
    width: 382px; height: 665px;
    border-radius: 22px; overflow: hidden;
    background: radial-gradient(ellipse at 50% 55%, var(--card-black-soft), var(--card-black) 70%);
    box-shadow: 0 6px 18px rgba(0,0,0,0.25);
  }
  .card-front { left: 199px; }
  .card-back { left: 619px; }
  .front-header { position: absolute; inset: 0; width: 382px; height: 665px; }
  .brand {
    position: absolute; display: flex; align-items: center; gap: 14px;
  }
  .brand-dot { width: 58px; height: 58px; border-radius: 50%; background: var(--mark-blue); }
  .brand-name { font-weight: 500; font-size: 56px; line-height: 1; letter-spacing: 1px; }
  .card-front .brand { left: 48px; top: 104px; }
  .card-front .brand-name { color: var(--ink); }
  .card-back .brand { left: 60px; top: 250px; }
  .card-back .brand-name { color: var(--text-light); }
  .contact { position: absolute; left: 40px; top: 372px; color: var(--text-light); }
  .person-name { font-size: 25px; font-weight: 500; }
  .person-title { font-size: 13.5px; color: var(--text-muted); margin-top: 6px; }
  .contact-list { list-style: none; margin-top: 12px; font-size: 15.5px; color: var(--text-muted); }
  .contact-list li { display: flex; align-items: center; gap: 8px; height: 23.5px; }
  .contact-list li.address { display: block; height: auto; line-height: 24px; margin: 12px 0 14px; }
  .contact-list svg { width: 15px; height: 15px; flex: none; fill: none; stroke: var(--text-light); stroke-width: 1.6; }
  .site-url {
    position: absolute; top: 390px; left: 0; width: 100%; text-align: center;
    color: var(--text-muted); font-size: 13px; letter-spacing: 3px;
  }
</style>
</head>
<body>
<main class="canvas">
  <section class="card card-front">
    <svg class="front-header" viewBox="0 0 382 665" aria-hidden="true">
      <path d="M0 0 H382 V196 Q200 232 0 178 Z" fill="var(--card-white)"/>
      <path d="M0 178 Q200 232 382 196 V214 Q200 250 0 194 Z" fill="var(--band-red)"/>
      <path d="M0 194 Q200 250 382 214 V220 Q200 256 0 199 Z" fill="var(--band-red-dark)"/>
    </svg>
    <div class="brand">
      <span class="brand-dot"></span>
      <span class="brand-name">DOVR</span>
    </div>
    <div class="contact">
      <h1 class="person-name">Tarek Demirci</h1>
      <p class="person-title">Senior Manager, Supply Chain</p>
      <ul class="contact-list">
        <li><svg viewBox="0 0 16 16"><path d="M3 2h3l1 4-2 1a8 8 0 0 0 4 4l1-2 4 1v3a1 1 0 0 1-1 1A12 12 0 0 1 2 3a1 1 0 0 1 1-1z"/></svg>(421)4820 3190</li>
        <li><svg viewBox="0 0 16 16"><rect x="1.5" y="3.5" width="13" height="9"/><path d="M1.5 3.5l6.5 5 6.5-5"/></svg>tdemirci@dovr.com</li>
        <li class="address">Office No 218, Saffron Crest Tower,<br>Palmera Bay Towers, Dubai, U.A.E</li>
        <li><svg viewBox="0 0 16 16"><rect x="2" y="6" width="12" height="8"/><path d="M4 6V2h6l2 2v2M5 9h2M5 11h2"/></svg>(405)618-2247 Ext 3190</li>
        <li><svg viewBox="0 0 16 16"><path d="M2 7c0-3 12-3 12 0v1h-3V6H5v2H2z"/><rect x="3" y="9" width="10" height="5"/></svg>(712)508-4431</li>
        <li><svg viewBox="0 0 16 16"><circle cx="8" cy="8" r="6.5"/><path d="M1.5 8h13M8 1.5c-3 3-3 10 0 13M8 1.5c3 3 3 10 0 13"/></svg>dovrtech.com</li>
      </ul>
    </div>
  </section>

  <section class="card card-back">
    <div class="brand">
      <span class="brand-dot"></span>
      <span class="brand-name">DOVR</span>
    </div>
    <p class="site-url">www.dovr.com</p>
  </section>
</main>
</body>
</html>
```